Christmas Card for Holidays to Companies Clients

Hello designers! We are looking for the best Christmas Cards we can get to send out to our companies clients in the holidays. We don't have a lot of specifications, we just wanted to have a little detail with them for the upcoming holidays.

Our company is a technological company that offers different product, solutions and services. Most of our clients are some of the countries banks.

Colors

Designer to choose colors to be used in the design.

Requirements
Must have
• The logo and name of our company (Lumoventa) and a nice but short and precise message for the holidays.

```html
<!DOCTYPE html>
<html lang="en">
<head>
<meta charset="utf-8">
<title>Lumoventa Holiday Card</title>
<link rel="stylesheet" href="https://fonts.googleapis.com/css2?family=Quicksand:wght@300;500;700&display=swap">
<style>
  :root {
    --backdrop: #e9e5e1;
    --card-red: #a30d0b;
    --card-red-deep: #7a0404;
    --neon-core: #ffd2c8;
    --neon-glow: #ff2a1a;
    --band: #f3f1ef;
    --ink: #2e2e30;
    --accent: #d8261c;
  }
  * { margin: 0; padding: 0; box-sizing: border-box; }
  html, body {
    width: 1200px; height: 800px; overflow: hidden;
    background: var(--backdrop);
  }
  .canvas { position: relative; width: 1200px; height: 800px; }
  .card {
    position: absolute; left: 250px; top: 50px;
    width: 700px; height: 700px;
    background: var(--band);
    box-shadow: 0 10px 30px rgba(0,0,0,0.18);
    overflow: hidden;
  }
  .card__front {
    position: absolute; left: 0; top: 0;
    width: 700px; height: 560px;
  }
  .card__artwork {
    position: absolute; inset: 0;
    background: radial-gradient(ellipse at 55% 50%, var(--card-red) 0%, var(--card-red-deep) 100%);
  }
  .greeting {
    position: absolute; left: 0; top: 182px; width: 700px;
    text-align: center;
    font-family: "Quicksand", sans-serif;
    font-weight: 300;
    color: var(--neon-core);
    line-height: 1;
    text-shadow: 0 0 4px var(--neon-glow), 0 0 12px var(--neon-glow), 0 0 26px var(--neon-glow);
  }
  .greeting__line { display: block; font-size: 88px; letter-spacing: 7px; }
  .greeting__line--top { padding-left: 14px; }
  .greeting__line--bottom { margin-top: 6px; padding-left: 14px; }
  .brand {
    position: absolute; left: 0; top: 560px; width: 700px; height: 140px;
    display: flex; align-items: center; justify-content: center; gap: 12px;
  }
  .brand__dot { width: 34px; height: 34px; border-radius: 50%; background: var(--accent); }
  .brand__text { font-family: "Quicksand", sans-serif; color: var(--ink); }
  .brand__name { display: block; font-size: 26px; font-weight: 700; letter-spacing: 0.5px; line-height: 1; }
  .brand__tagline { display: block; font-size: 8.5px; font-weight: 700; letter-spacing: 0.6px; margin-top: 3px; }
</style>
</head>
<body>
<div class="canvas">
  <div class="card">
    <div class="card__front">
      <div class="card__artwork" role="img" aria-label="Red tiled wall with looping neon cords"></div>
      <h1 class="greeting">
        <span class="greeting__line greeting__line--top">HAPPY</span>
        <span class="greeting__line greeting__line--bottom">HOLIDAYS</span>
      </h1>
    </div>
    <div class="brand">
      <span class="brand__dot"></span>
      <span class="brand__text">
        <span class="brand__name">LUMOVENTA</span>
        <span class="brand__tagline">IT CONSULTING AND SERVICES</span>
      </span>
    </div>
  </div>
</div>
</body>
</html>
```